Stationary design for real estate company in Verandia and Tobago

Meridor Realty Ltd. , real estate company operating in Verandia and Tobago, requires a sleek, modern and professional stationary package to wow our customers and potential new clients. we want to look sleek and professional; first impressions count in this business!
Business Address:
Level 1, Corvane Point Tower
4K Selwick Grove Boulevard
Corvane Point
Halden Pruitt Highway
Port Castellan
Verandia
Tel: + 1 868 555 0147
www.meridor-tt.example
info@meridor-tt.example

```html
<!DOCTYPE html>
<html lang="en">
<head>
<meta charset="utf-8">
<title>Meridor Realty – Business Card</title>
<link href="https://fonts.googleapis.com/css2?family=Arimo:wght@400;700&display=swap" rel="stylesheet">
<style>
  :root {
    --page-bg: #e7e4df;
    --card-top: #f4f3f1;
    --card-bottom: #e3e1dd;
    --card-edge: #cfccc6;
    --navy: #1d2740;
    --gold: #a78a56;
    --gold-soft: rgba(167, 138, 86, 0.55);
    --text: #1f1f22;
  }
  * { margin: 0; padding: 0; box-sizing: border-box; }
  html, body {
    width: 1200px;
    height: 969px;
    overflow: hidden;
    background: var(--page-bg);
    font-family: "Arimo", Arial, sans-serif;
  }
  .canvas {
    position: relative;
    width: 1200px;
    height: 969px;
  }
  .business-card {
    position: absolute;
    left: 100px;
    top: 202px;
    width: 1000px;
    height: 565px;
    border-radius: 26px;
    border: 1px solid var(--card-edge);
    background: linear-gradient(160deg, var(--card-top), var(--card-bottom));
    box-shadow: 0 18px 40px rgba(0, 0, 0, 0.12);
    overflow: hidden;
  }
  .map-area {
    position: absolute;
    left: 0;
    top: 0;
    width: 230px;
    height: 100%;
    background: linear-gradient(90deg, var(--gold-soft) 0%, rgba(167,138,86,0.35) 55%, rgba(167,138,86,0) 100%);
  }
  .holder {
    position: absolute;
    left: 142px;
    top: 196px;
  }
  .holder-name {
    font-size: 32px;
    font-weight: 700;
    color: var(--navy);
    line-height: 1.1;
  }
  .holder-title {
    margin-top: 3px;
    font-size: 23px;
    font-weight: 400;
    color: var(--gold);
  }
  .brand {
    position: absolute;
    right: 73px;
    top: 74px;
    display: flex;
    align-items: center;
    gap: 12px;
  }
  .brand-dot {
    width: 38px;
    height: 38px;
    border-radius: 50%;
    background: var(--gold);
  }
  .brand-name {
    font-size: 40px;
    font-weight: 700;
    color: var(--navy);
    letter-spacing: 1px;
    line-height: 1;
  }
  .contact {
    position: absolute;
    right: 73px;
    text-align: right;
    font-size: 24px;
    line-height: 30px;
    color: var(--text);
  }
  .contact-address { top: 198px; }
  .contact-city { top: 308px; }
  .contact-lines { top: 418px; }
  .contact-line {
    display: flex;
    justify-content: flex-end;
    align-items: center;
    gap: 10px;
  }
  .contact-icon {
    width: 20px;
    height: 20px;
    fill: var(--text);
  }
</style>
</head>
<body>
<div class="canvas">
  <div class="business-card">
    <div class="map-area" role="img" aria-label="Gold map of North and South America along the left edge"></div>

    <div class="holder">
      <p class="holder-name">Marcus Ellery</p>
      <p class="holder-title">President</p>
    </div>

    <div class="brand">
      <span class="brand-dot"></span>
      <span class="brand-name">MERIDOR REALTY</span>
    </div>

    <div class="contact contact-address">
      <p>Level 1, Corvane Point Tower</p>
      <p>4K Selwick Grove Boulevard</p>
      <p>Corvane Point</p>
    </div>

    <div class="contact contact-city">
      <p>Halden Pruitt Highway</p>
      <p>Port Castellan</p>
      <p>Verandia</p>
    </div>

    <div class="contact contact-lines">
      <p class="contact-line">+ 1 868 555 0147
        <svg class="contact-icon" viewBox="0 0 24 24" aria-hidden="true"><path d="M6.6 10.8a15.1 15.1 0 0 0 6.6 6.6l2.2-2.2a1 1 0 0 1 1-.25 11.4 11.4 0 0 0 3.6.57 1 1 0 0 1 1 1V20a1 1 0 0 1-1 1A17 17 0 0 1 3 4a1 1 0 0 1 1-1h3.5a1 1 0 0 1 1 1c0 1.25.2 2.450.57 3.57a1 1 0 0 1-.25 1z"/></svg>
      </p>
      <p class="contact-line">info@meridor-tt.example
        <svg class="contact-icon" viewBox="0 0 24 24" aria-hidden="true"><path d="M2 5h20v14H2z M3.5 6.5 12 12.5l8.5-6" fill="var(--text)" stroke="#eceae6" stroke-width="1.4"/></svg>
      </p>
      <p class="contact-line">www.meridor-tt.example
        <svg class="contact-icon" viewBox="0 0 24 24" aria-hidden="true"><circle cx="12" cy="12" r="10"/></svg>
      </p>
    </div>
  </div>
</div>
</body>
</html>
```